Corporate flyer highlighting service offering for PR agency

A corporate flyer is needed for a new service offering that we are doing. The product name is HarborLeap it is a marketing and communications services offering for companies who are getting ready to sell their business. If we are really happy with the designer's work, there will be a great deal more projects. I am looking for a clean design with a few pops of color from my site. https://quillmarsh.partners. I am looking for a good design with data in sections. I am looking for a clean design that feels high-end but not cluttered. Please do not use images of people. Please see the following examples of types of designs I like.
https://www.tackboard.example/pin/839201746530918264/
https://www.tackboard.example/pin/402918375561029847/
https://assets.stockvale.example/corporate-flyer-template-KRTPMB
https://designbrook.example/item/corporate-flyer-template/81046395?s_rank=8
https://assets.stockvale.example/corporate-business-flyer-template-93PX7D

I had to place the project on hold as I choose the wrong type of project and did not get many designs as a result. I am reposting this with an updated brief.

Target Market(s)

Business sellers and brokers

Industry/Entity Type

Marketing for business sellers

Font styles to use
Sans Serif

Requirements
Must have
• Good quality design with content in sections. Clean and high end feeling is a must.
Should not have
• A lot of images of people.

```html
<!DOCTYPE html>
<html lang="en">
<head>
<meta charset="utf-8">
<title>HarborLeap Flyer – Quillmarsh Partners</title>
<link rel="stylesheet" href="https://fonts.googleapis.com/css2?family=Montserrat:wght@500;600;700;800&family=Open+Sans:wght@400;600;700&display=swap">
<style>
:root{
  --navy:#17354f;
  --navy-deep:#122b41;
  --blue:#2c87c8;
  --sky:#3aa6e6;
  --orange:#ee5a22;
  --green:#69a83a;
  --yellow:#f3b41b;
  --lime:#8cc63f;
  --ink:#27313a;
  --paper:#ffffff;
  --table:#5b5c5e;
}
*{box-sizing:border-box;margin:0;padding:0}
html,body{width:1200px;height:775px;overflow:hidden}
body{background:var(--table);font-family:"Open Sans",Arial,sans-serif;color:var(--ink);position:relative}
.page{position:absolute;top:15px;width:572px;height:745px;background:var(--paper);overflow:hidden;box-shadow:0 4px 14px rgba(0,0,0,.35)}
.page--front{left:18px}
.page--back{left:610px}
ul{list-style:none}
.checks li{position:relative;padding-left:12px;margin-bottom:3px}
.checks li::before{content:"✓";position:absolute;left:0;top:2px;width:8px;height:8px;border-radius:50%;background:var(--sky);color:#fff;font-size:5.5px;line-height:8px;text-align:center;font-weight:700}
.on-blue .checks li::before,.on-green .checks li::before{background:#fff;color:var(--blue)}
.on-green .checks li::before{color:var(--green)}

/* brand */
.brand{display:flex;align-items:center;gap:7px}
.brand__mark{width:14px;height:14px;background:var(--orange)}
.brand__name{font-family:"Montserrat",Arial,sans-serif;font-weight:600;font-size:15px;letter-spacing:.5px;color:#fff;text-transform:uppercase;line-height:1}

/* header */
.hero{position:absolute;left:0;top:0;width:572px;height:180px;background:var(--navy)}
.hero__photo{position:absolute;right:0;top:0;width:330px;height:180px;background:linear-gradient(160deg,#7fb3dc 0%,#b9cfdf 35%,#9a7a62 62%,#4d6a45 85%,#2f4a3b 100%);clip-path:polygon(30% 0,100% 0,100% 100%,0 100%)}
.hero .brand{position:absolute;left:28px;top:30px}
.hero__title{position:absolute;left:28px;top:62px;width:360px;font-family:"Montserrat",Arial,sans-serif;font-weight:700;font-size:13px;line-height:1.25}
.hero__title .t1{color:var(--sky)}
.hero__title .t2{color:var(--yellow)}
.hero__title .t3{color:var(--lime)}
.hero__intro{position:absolute;left:28px;top:116px;width:330px;color:#fff;font-size:6.4px;line-height:1.35}
.hero__intro p+p{margin-top:4px}

/* front body */
.front-left{position:absolute;left:0;top:180px;width:232px;height:520px;padding:8px 14px 0 22px;font-size:6.9px;line-height:1.4}
.callout{padding:7px 9px;font-size:6.8px;line-height:1.35;color:#fff}
.callout--orange{background:var(--orange);font-style:italic}
.callout--green{background:var(--green)}
.callout--green .split{display:grid;grid-template-columns:1fr 1fr;margin:4px 0}
.front-left .lead{margin-top:9px}
.front-left .strong{margin-top:9px;font-weight:700;font-size:7.4px;line-height:1.35}
.front-left .checks{margin-top:8px}
.front-right{position:absolute;left:232px;top:180px;width:340px;height:520px;background:var(--blue);color:#fff;padding:12px 20px 0 16px;font-size:7.6px;line-height:1.4}
.on-blue h3{font-family:"Montserrat",Arial,sans-serif;font-size:8.4px;font-weight:700;margin:10px 0 3px}
.front-right h3{font-size:9px;margin-top:14px}
.front-right .intro{font-weight:600}
.front-right .sub{font-weight:700}
.front-right .checks li{margin-bottom:9px}
.front-right .checks li strong{font-size:8.2px;display:block}
.front-right .stats{margin-top:18px}
.front-right .stats li{margin-bottom:12px}

/* footer */
.footer{position:absolute;left:0;bottom:0;width:100%;height:45px;background:var(--navy-deep);display:flex;align-items:center;gap:22px;padding-left:24px;color:#fff;font-family:"Montserrat",Arial,sans-serif;font-weight:600;font-size:9.5px}
.footer__item{display:flex;align-items:center;gap:6px}
.footer__icon{width:14px;height:14px}

/* back */
.back-left{position:absolute;left:0;top:0;width:300px;height:700px;background:var(--blue);color:#fff;padding:28px 16px 0 24px;font-size:7.4px;line-height:1.4}
.back-left h3:first-child{margin-top:0}
.back-left h3{margin-top:22px}
.back-left .checks{margin-top:6px}
.back-left .checks li{margin-bottom:5px}
.back-left .nested{margin-left:10px;margin-top:4px}
.back-right{position:absolute;left:300px;top:0;width:272px;height:700px;padding:20px 20px 0 16px;font-size:7.1px;line-height:1.4}
.back-right h4{font-family:"Montserrat",Arial,sans-serif;font-size:7.6px;font-weight:700}
.quote{margin:14px 0 0 6px;border:2px solid var(--blue);background:var(--orange);color:#fff;padding:10px 10px 8px;font-size:8.4px;line-height:1.35;position:relative}
.quote::before{content:"\201C";position:absolute;left:-8px;top:-12px;font-family:"Montserrat",Arial,sans-serif;font-size:24px;color:var(--blue);font-weight:800}
.quote::after{content:"\201D";position:absolute;right:-6px;bottom:-20px;font-family:"Montserrat",Arial,sans-serif;font-size:24px;color:var(--blue);font-weight:800}
.quote cite{display:block;text-align:right;font-style:normal;font-size:7.4px;margin-top:2px}
.workbox{margin-top:20px;background:var(--green);color:#fff;padding:9px 10px;font-size:6.8px;line-height:1.4}
.workbox .checks{margin-top:6px}
.workbox .checks li{margin-bottom:7px}
.back-right .closing p{margin-top:9px}
.back-right .closing{margin-top:8px}
.back-right .brand{margin-top:22px;justify-content:center}
.back-right .brand__name{color:var(--navy)}
</style>
</head>
<body>

<section class="page page--front">
  <header class="hero">
    <div class="hero__photo" role="img" aria-label="Aerial photograph of a city skyline with a river and bridge"></div>
    <div class="brand"><span class="brand__mark"></span><span class="brand__name">Quillmarsh Partners</span></div>
    <h1 class="hero__title">
      <span class="t1">HarborLeap provides executives and</span><br>
      <span class="t2">business owners with clear guidance to</span><br>
      <span class="t3">unlock non-financial value ahead of an exit.</span>
    </h1>
    <div class="hero__intro">
      <p>A strong communication and marketing strategy can significantly increase the value of your business leading up to an exit. Buyers are looking to mitigate risk and unlock potential value as a catalyst for clear growth potential.</p>
      <p>Highlighting your company's success in the marketplace, identifying, and mitigating reptation risks before buyers do, enhancing employee engagement, finding hidden opportunities to boost marketing KPIs and showcasing IP, data, and innovation, can make a significant difference in valuation.</p>
    </div>
  </header>

  <div class="front-left">
    <p class="callout callout--orange">US institutional investors believe that Investor Relations (IR) accounts for a total variance of 30% in a company's valuation – from a premium of 10% for "superb" IR to a discount of 20% for "poor" IR. ---Corvane Research Group, "Harnessing IR's Power to Impact a Company's Valuation."</p>
    <div class="callout callout--green on-green">
      <p>We design and implement communication and marketing strategies that deliver significant increases in brand awareness, identify reputational risks, and enhance brand perception, helping owners and investors to realize premium values for their companies. We support owners and companies through:</p>
      <div class="split">
        <ul class="checks"><li>Company Exit Preparation</li><li>M&amp;A</li><li>IPO</li></ul>
        <ul class="checks"><li>Spinoff/Divestiture</li><li>New Leadership/Investor</li></ul>
      </div>
      <p>Few sellers would list their home without first inspecting, repairing broken items, and making updates to highlight the positive aspects --increasing appeal to buyers. However, countless business owners leavemoney on the table during corporate exits due to a lack of preparation.</p>
    </div>
    <p class="lead">Our team of executive-level communications and marketing experts brings deep buy and sell-side experience. We have played critical roles in the acquisition, integration and disposition process. Our mix of financial services expertise combined with decades of experience leading internal and external communications, marketing and investor relations teams gives us a unique perspective on identifying and unlocking non-financial areas of value and mitigatingnon-financial risksbefore exit.</p>
    <p class="strong">While accounting and investment banking teams are hard at work increasing value from a financial perspective, we help organizations enhance their valuation by identifying areas that will appeal most to buyers and ensuring those elements of your business are visible and memorable to those who matter most.</p>
    <ul class="checks">
      <li>Highlighting value in a clear and visible way</li>
      <li>Streamlining the exit process</li>
      <li>Identifying potential risks and suggesting mitigation measures</li>
      <li>Creating a polished presence in the market ahead of buyer interest</li>
    </ul>
  </div>

  <div class="front-right on-blue">
    <p class="intro">HarborLeap provides executives and business owners with clear guidance to unlock value ahead of an exit. Our non-disruptive, ala-carte process enables us to work with sellers on specific areas or to do a complete analysis and recommendation and can include:</p>
    <h3>Brand Analysis and Recommendations</h3>
    <p class="sub">Strong brands command a higher valuation. We conduct a brand analysis, providing clear &amp; detailed recommendations to enhance your value proposition and help you stand out from the crowd:</p>
    <ul class="checks" style="margin-top:7px">
      <li><strong>Current external position among competitors--</strong>We look at how your brand measures up based on external competitive analysis, positioning in the media and analyst community, and across other digital channels.</li>
      <li><strong>Physical brand image--</strong>A little bit of paint and updated fixtures can go a long way when increasing the value of a home. The same is true for businesses. Our audit evaluates non-disruptive steps your company can take to enhance your brand look and feel before sale.</li>
      <li><strong>Employee brand perception--</strong>We conduct a high-level external audit with recommendations to enhance engagement for current and prospective employees.</li>
      <li><strong>Customer brand perception--</strong>We conduct a high-level external audit showcasing how customers perceive your brand in the market. We then provide recommendations for enhancing engagement and maximizing value.</li>
    </ul>
    <ul class="checks stats">
      <li>A 5% increase in customer retention correlates with at least a 25% increase in profit, according to an analysis by Halden &amp; Company. <strong>(https://media.haldenco.example/docs/retention_cutting_costs.pdf)</strong></li>
      <li>It costs 5 times more to acquire a new customer than to retain a current one and 16 times more to get new customers to the same spending level as existing ones. <strong>(https://growthledger.example/customer-retention-guide-statistics/)</strong></li>
    </ul>
  </div>

  <footer class="footer">
    <span class="footer__item"><svg class="footer__icon" viewBox="0 0 14 14"><circle cx="7" cy="7" r="7" fill="#ee5a22"/><path d="M7 3.2a2.4 2.4 0 0 0-2.4 2.4C4.6 7.5 7 10.6 7 10.6s2.4-3.1 2.4-5A2.4 2.4 0 0 0 7 3.2z" fill="#fff"/><circle cx="7" cy="5.6" r=".9" fill="#ee5a22"/></svg>Fernwick</span>
    <span class="footer__item"><svg class="footer__icon" viewBox="0 0 14 14"><circle cx="7" cy="7" r="7" fill="#ee5a22"/><rect x="3.5" y="4.5" width="7" height="5" fill="none" stroke="#fff" stroke-width="1"/><path d="M3.5 4.5 7 7.3l3.5-2.8" fill="none" stroke="#fff" stroke-width="1"/></svg>info@quillmarsh.partners</span>
    <span class="footer__item"><svg class="footer__icon" viewBox="0 0 14 14"><circle cx="7" cy="7" r="7" fill="#ee5a22"/><circle cx="7" cy="7" r="3.6" fill="none" stroke="#fff" stroke-width=".9"/><path d="M3.4 7h7.2M7 3.4c-1.8 2-1.8 5.2 0 7.2M7 3.4c1.8 2 1.8 5.2 0 7.2" fill="none" stroke="#fff" stroke-width=".8"/></svg>https://quillmarsh.partners</span>
  </footer>
</section>

<section class="page page--back">
  <div class="back-left on-blue">
    <h3>Digital and Traditional Marketing Analysis and Recommendations</h3>
    <p>How much money are you leaving on the table? Our marketing audits help organizations identify areas of hidden value that can have significant impacts on revenue and valuation. We optimize current activities and uncover new strategies to increase the effectiveness of current marketing spend. Areas we evaluate include:</p>
    <ul class="checks">
      <li>Website traffic and conversion</li>
      <li>CRM process review to identify strategies &amp; recommendations to increase conversion and reactive old-leads</li>
      <li>Email marketing strategy</li>
      <li>Automations and drip marketing</li>
      <li>Social media strategy /presence</li>
      <li>Partnership marketing</li>
      <li>Paid media analysis/strategy suggestion</li>
    </ul>
    <h3>Messaging and Content Strategy Review and Analysis</h3>
    <p>It's about your valuation. Full and fair valuation requires a clear, compelling investment case articulated consistently to the right audience at the right time. Messaging to maximize your value in an acquisition or an IPO is quite different from typical selling messages for prospects, customers, or 'features &amp; business benefits' for press and analysts. We understand the issues and speak the right language to maximize perception of value with key decision makers.</p>
    <ul class="checks">
      <li>Review and recommendations of key messaging and value proposition</li>
      <li>Analysis and recommendations to highlight data, IP, and innovation</li>
      <li>Analysis and recommendations to position key executives likely to remain with the company as thought leaders to help build value</li>
      <li>Analysis and recommendations to build employee engagement and retention enhancing your most valuable asset-your team</li>
    </ul>
    <h3>Media and Analyst Strategy Development</h3>
    <p>Positive articles and inclusion in analyst reports pack a powerful punch when preparing your business for sale. We work with clients to develop a media strategy that goes beyond brand awareness, leveraging media to build a digital history of third-party validation targeted to enhance appeal to prospective buyers while generating traffic and connections, to enhance overall value.</p>
    <ul class="checks">
      <li>Positioning to media and analyst community creating third party market validation</li>
      <li>Key angle recommendations</li>
      <li>Announcement timeline &amp; strategy planning to maximize media value of news
        <ul class="checks nested">
          <li>What is newsworthy</li>
          <li>How to position that news for the most significant impact</li>
        </ul>
      </li>
    </ul>
  </div>

  <div class="back-right">
    <h4>"White Hat/Black Hat Review"</h4>
    <p>We take a buyer's communications and marketing approach to analyzing the client company and provide a "punch list" of things a potential buyer is likely to ask/request in due diligence from a comms/culture/marketing/reputation standpoint to ensure that when potential buyers start screening for sellers and evaluating them, the client company has the upper hand.</p>
    <blockquote class="quote">Strategy without tactics is the slowest route to victory. Tactics without strategy is the noise before defeat.<cite>– Oren Vask</cite></blockquote>
    <div class="workbox on-green">
      <p><strong>Once the analysis is complete, we deliver actionable intelligence and recommendations to help leaders identify and quickly unlock areas that will boost value and appeal to prospective buyers. Work products include:</strong></p>
      <ul class="checks">
        <li><strong>Gap Assessment --</strong> We provide a comprehensive seller report providing analysis and actionable recommendations to increase your valuation while identifying and mitigating non-financial risks.</li>
        <li><strong>Strategic Roadmap --</strong> Clients are given an actionable tactical roadmap based on the recommendation provided. Organizations can choose to implement key areas or include this powerful guide as part of their presentation to prospective buyers to highlight latent potential. The roadmap provides actionable steps buyers can take upon close as they make their case for your business with their investment committees.</li>
      </ul>
    </div>
    <div class="closing">
      <p>Once the strategy integration roadmap is complete, your team can implement it on your timeline, we can work with your team providing guidance and executive-level support, or we can fully execute deliverables with our robust capabilities and team.</p>
      <p>Our value proposition, based on delivering outcomes rather than just outputs, means that you receive the benefit and capability of deeply experienced corporate communications leaders without adding headcount or the time to identify, recruit, onboard and retain a new team member.</p>
      <p>We help organizations enhance their valuation by identifying areas that will appeal most to buyers and ensuring those elements of your business are visible and memorable to those who matter most.</p>
      <p>HarborLeap helps sellers maximize valuation and unlock hidden potential ahead of an exit--ensuring money is not left on the table.</p>
    </div>
    <div class="brand"><span class="brand__mark"></span><span class="brand__name">Quillmarsh Partners</span></div>
  </div>

  <footer class="footer">
    <span class="footer__item"><svg class="footer__icon" viewBox="0 0 14 14"><circle cx="7" cy="7" r="7" fill="#ee5a22"/><path d="M7 3.2a2.4 2.4 0 0 0-2.4 2.4C4.6 7.5 7 10.6 7 10.6s2.4-3.1 2.4-5A2.4 2.4 0 0 0 7 3.2z" fill="#fff"/><circle cx="7" cy="5.6" r=".9" fill="#ee5a22"/></svg>Fernwick</span>
    <span class="footer__item"><svg class="footer__icon" viewBox="0 0 14 14"><circle cx="7" cy="7" r="7" fill="#ee5a22"/><rect x="3.5" y="4.5" width="7" height="5" fill="none" stroke="#fff" stroke-width="1"/><path d="M3.5 4.5 7 7.3l3.5-2.8" fill="none" stroke="#fff" stroke-width="1"/></svg>info@quillmarsh.partners</span>
    <span class="footer__item"><svg class="footer__icon" viewBox="0 0 14 14"><circle cx="7" cy="7" r="7" fill="#ee5a22"/><circle cx="7" cy="7" r="3.6" fill="none" stroke="#fff" stroke-width=".9"/><path d="M3.4 7h7.2M7 3.4c-1.8 2-1.8 5.2 0 7.2M7 3.4c1.8 2 1.8 5.2 0 7.2" fill="none" stroke="#fff" stroke-width=".8"/></svg>https://quillmarsh.partners</span>
  </footer>
</section>

</body>
</html>
```